Nebelkreis - needs a CD/Cover Design for a VA Compilation

We need a CD-Design/Cover-Artwork for our Various Artists Compilation called 'Nebelkreis', which means "Fog circle". Back then our events were based in one of Germanys best underground techno-clubs., which we also called "our temple".
The artists featured on this compilation rather performed at our events or had a massive influence on the music the djs played.
The sound is glitchy, technically detailed and a little unpredictable.

We would like to see some designs not too colourful!

Target Market(s)

complex electronic music listeners

Industry/Entity Type

Club

Font styles to use
Sans Serif

Colors
ec1f27

Requirements
Must have
• Ideally the artwork should be something otherworldly, abstract/glitchy, be an optical illusion and/or have geometric complexity.
Nice to have
• - probably black and white design fits better with us, but you can also try it with a very few colors.
- maybe something futuristic or scatchy
Should not have
• - it should definitely NOT be too colourful.
- no humans!! or animals
- in case you think to draw a temple, please use it more abstract, nothing too obviously, we dont wanna look like a hippie event!
- no musical notes
- no obvious "play" symbol / headphones or vinyl images

```html
<!DOCTYPE html>
<html lang="de">
<head>
<meta charset="utf-8">
<title>Nebelkreis – Various Artists Compilation</title>
<link href="https://fonts.googleapis.com/css2?family=Barlow+Semi+Condensed:wght@600&family=Barlow:wght@400&display=swap" rel="stylesheet">
<style>
  :root {
    --bg: #2a2222;
    --white: #f4f2f1;
    --red: #ec1f27;
    --grey: #cfcaca;
  }
  html, body {
    margin: 0;
    padding: 0;
    overflow: hidden;
    background: var(--bg);
  }
  .cover {
    position: relative;
    width: 1200px;
    height: 1200px;
    background: var(--bg);
    overflow: hidden;
  }
  .emblem {
    position: absolute;
    left: 180px;
    top: 160px;
    width: 830px;
    height: 630px;
  }
  .subtitle {
    position: absolute;
    top: 872px;
    left: 526px;
    margin: 0;
    font-family: "Barlow", sans-serif;
    font-weight: 400;
    font-size: 20px;
    letter-spacing: 3.2px;
    color: var(--grey);
    white-space: nowrap;
  }
  .title-block {
    position: absolute;
    left: 253px;
    top: 896px;
    width: 660px;
    height: 130px;
  }
  .title,
  .title-echo {
    position: absolute;
    left: 0;
    top: 0;
    margin: 0;
    font-family: "Barlow Semi Condensed", sans-serif;
    font-weight: 600;
    font-size: 132px;
    line-height: 130px;
    letter-spacing: -4px;
    white-space: nowrap;
  }
  .title .part-light,
  .title-echo .part-light { color: var(--white); }
  .title .part-red,
  .title-echo .part-red { color: var(--red); }
  .title-echo {
    opacity: 0.22;
    filter: blur(6px);
    transform-origin: top left;
  }
  .title-echo--above { transform: translate(-10px, -60px) scaleY(0.9); }
  .title-echo--below { transform: translate(0, 95px) scaleY(1.05); opacity: 0.14; }
</style>
</head>
<body>
  <main class="cover">
    <svg class="emblem" viewBox="0 0 830 630" role="img" aria-label="Geometric star mandala: a white twelve-pointed star inside a dashed ring, with a faded red echo of the same mandala offset to the left">
      <defs>
        <radialGradient id="echo-glow" cx="50%" cy="50%" r="50%">
          <stop offset="0%" stop-color="#ec1f27" stop-opacity="0.28"/>
          <stop offset="70%" stop-color="#ec1f27" stop-opacity="0.12"/>
          <stop offset="100%" stop-color="#ec1f27" stop-opacity="0"/>
        </radialGradient>
        <radialGradient id="main-glow" cx="50%" cy="50%" r="50%">
          <stop offset="0%" stop-color="#f4f2f1" stop-opacity="0.38"/>
          <stop offset="70%" stop-color="#f4f2f1" stop-opacity="0.14"/>
          <stop offset="100%" stop-color="#f4f2f1" stop-opacity="0"/>
        </radialGradient>
      </defs>
      <ellipse cx="300" cy="313" rx="290" ry="300" fill="url(#echo-glow)"/>
      <ellipse cx="517" cy="313" rx="300" ry="305" fill="url(#main-glow)"/>
    </svg>

    <p class="subtitle">VARIOUS ARTISTS COMPILATION</p>

    <div class="title-block">
      <div class="title-echo title-echo--above" aria-hidden="true"><span class="part-light">NEBEL</span><span class="part-red">KREIS</span></div>
      <div class="title-echo title-echo--below" aria-hidden="true"><span class="part-light">NEBEL</span><span class="part-red">KREIS</span></div>
      <h1 class="title"><span class="part-light">NEBEL</span><span class="part-red">KREIS</span></h1>
    </div>
  </main>
</body>
</html>
```